Spiral Bound Classy Marketing Planner Cover Design

A5 marketing planner book cover requiredClassy, minimalist design for female entrepreneurs. The inside is all in grey and is a minimalist uncluttered design. Name of the planner is It's Time Marketing Recipe PlannerHeader font inside the planner is Shelby and other font is Lato Brand colours are teal and grey.The printing format has changed and as such I am looking for a new cover design to make this marketing planner look classy and engaging. Would prefer my logo to be on the back. We have the option for a 10cm x 10cm foil detail to be added on the front cover, feel free to add this to your design.This is for a spiral bound book - A5 front cover and A5 back cover - no spine required.

Target Market(s)

Female entrepreneurs

Industry/Entity Type

Marketing

Colors
33b8a4
ffffff

Requirements
Must have
• Front and back designs
• A5
Should not have
• Large illustrations
• People in the design
• Spine design

```html
<!DOCTYPE html>
<html lang="en">
<head>
<meta charset="utf-8">
<title>Bright Path Promotion Blueprint Planner — Front Cover</title>
<link href="https://fonts.googleapis.com/css2?family=Cormorant+Garamond:ital,wght@1,500&family=Open+Sans:wght@600&display=swap" rel="stylesheet">
<style>
  :root {
    --teal: #33b8a4;
    --grey: #88868a;
    --paper: #ffffff;
  }
  * { margin: 0; padding: 0; box-sizing: border-box; }
  html, body {
    width: 1200px;
    height: 1200px;
    overflow: hidden;
    background: var(--paper);
  }
  .front-cover {
    position: relative;
    width: 1200px;
    height: 1200px;
    background: var(--paper);
  }
  .bookmark-ribbon {
    position: absolute;
    left: 0;
    top: 0;
    width: 1200px;
    height: 360px;
  }
  .planner-title {
    position: absolute;
    left: 0;
    width: 1200px;
    text-align: center;
    white-space: nowrap;
  }
  .planner-title__script {
    top: 332px;
    padding-left: 8px;
    font-family: "Cormorant Garamond", Georgia, serif;
    font-style: italic;
    font-weight: 500;
    font-size: 58px;
    line-height: 80px;
    color: var(--grey);
  }
  .planner-title__caps {
    top: 448px;
    padding-left: 16px;
    font-family: "Open Sans", Arial, sans-serif;
    font-weight: 600;
    font-size: 27px;
    line-height: 40px;
    letter-spacing: 0;
    text-transform: uppercase;
    color: var(--teal);
  }
</style>
</head>
<body>
  <main class="front-cover">
    <svg class="bookmark-ribbon" viewBox="0 0 1200 360" aria-hidden="true">
      <defs>
        <filter id="ribbon-shadow" x="-30%" y="-10%" width="160%" height="130%">
          <feGaussianBlur in="SourceAlpha" stdDeviation="6"/>
          <feOffset dx="7" dy="6" result="blur"/>
          <feComponentTransfer><feFuncA type="linear" slope="0.4"/></feComponentTransfer>
          <feMerge><feMergeNode/><feMergeNode in="SourceGraphic"/></feMerge>
        </filter>
      </defs>
      <polygon points="519,0 674,0 674,318 598,288 519,318" fill="var(--teal)" filter="url(#ribbon-shadow)"/>
    </svg>
    <h1 class="planner-title planner-title__script">Bright Path</h1>
    <p class="planner-title planner-title__caps">Promotion Blueprint Planner</p>
  </main>
</body>
</html>
```